Please create a custom business card for 'Adventures beyond any map'. The logo is attached to this brief.

Here is the link to the logo project : http://work.plumvessel.example/task.aspx?id=319207

Questions can be posted on the Discussion Board.

```html
<!DOCTYPE html>
<html lang="en">
<head>
<meta charset="utf-8">
<title>Mapless — Business Card</title>
<link rel="stylesheet" href="https://fonts.googleapis.com/css2?family=Exo+2:wght@400;600;700&display=swap">
<style>
  :root {
    --stage: #2b2622;
    --card: #050505;
    --brand-red: #ee1c1c;
    --deep-red: #9a1a16;
    --ink-white: #ffffff;
    --ink-grey: #8a8a8a;
  }
  * { margin: 0; padding: 0; box-sizing: border-box; }
  html, body { width: 1200px; height: 900px; overflow: hidden; }
  body {
    background: var(--stage);
    font-family: "Exo 2", "Arial", sans-serif;
    position: relative;
  }
  .card {
    position: absolute;
    width: 600px;
    height: 343px;
    background: var(--card);
    box-shadow: 0 18px 40px rgba(0,0,0,.55);
    overflow: hidden;
  }
  .card--front { left: 150px; top: 80px; }
  .card--back  { left: 450px; top: 480px; }

  .brand {
    display: flex;
    align-items: center;
    gap: 12px;
    color: var(--brand-red);
    font-weight: 700;
    letter-spacing: 1px;
  }
  .brand__mark { background: var(--brand-red); }

  .card--front .brand {
    position: absolute;
    left: 50%; top: 50%;
    transform: translate(-50%, -50%);
    font-size: 62px;
  }
  .card--front .brand__mark { width: 40px; height: 40px; }

  .card--back .brand {
    position: absolute;
    left: 34px; top: 34px;
    font-size: 38px;
  }
  .card--back .brand__mark { width: 24px; height: 24px; }

  .feature-shape {
    position: absolute;
    right: -40px; top: 40px;
    width: 270px; height: 270px;
    border-radius: 50%;
    background: linear-gradient(135deg, var(--brand-red) 55%, var(--deep-red));
  }

  .person { position: absolute; left: 40px; top: 120px; }
  .person__name { color: var(--brand-red); font-size: 24px; font-weight: 700; line-height: 1.1; }
  .person__role { color: var(--ink-grey); font-size: 15px; font-weight: 600; }

  .contact {
    position: absolute; left: 40px; top: 188px;
    list-style: none;
    color: var(--ink-white);
    font-size: 16px; font-weight: 600;
    line-height: 1.45;
  }
  .contact li { display: flex; align-items: center; gap: 10px; }
  .contact svg { width: 14px; height: 14px; fill: none; stroke: var(--brand-red); stroke-width: 2; }

  .address {
    position: absolute; left: 64px; top: 270px;
    color: var(--ink-white);
    font-size: 16px; font-weight: 600;
    font-style: normal; line-height: 1.35;
  }
</style>
</head>
<body>
  <section class="card card--front">
    <div class="brand"><span class="brand__mark"></span>Mapless</div>
  </section>

  <section class="card card--back">
    <div class="brand"><span class="brand__mark"></span>Mapless</div>
    <div class="feature-shape" aria-hidden="true"></div>

    <div class="person">
      <p class="person__name">Dana Reyes</p>
      <p class="person__role">Managing Director</p>
    </div>

    <ul class="contact">
      <li><svg viewBox="0 0 16 16"><path d="M4 2l3 3-2 2c1 2 2 3 4 4l2-2 3 3-2 2C6 14 2 10 2 4z"/></svg>+123 555 0142</li>
      <li><svg viewBox="0 0 16 16"><rect x="1.5" y="3.5" width="13" height="9"/><path d="M1.5 3.5l6.5 5 6.5-5"/></svg>dana@mapless.example</li>
      <li><svg viewBox="0 0 16 16"><rect x="1.5" y="2.5" width="13" height="9"/><path d="M5 14.5h6M8 11.5v3"/></svg>www.mapless.example</li>
    </ul>

    <address class="address">48 Harbor Lane, Suite 2,<br>Town, NY 10231</address>
  </section>
</body>
</html>
```